New Zealand health product business needs website designed

A website is required for a business that sells New Zealand made products, namely products like infant formula, health products such as NZ honey, supplements, skincare products etc. This is purely an informative website that will introduce the all the different types of products the business has to offer. The target audience will the the Chinese market. The logo is a calligraphy style font in colours 78b643 and 313542 (logo is still being finalised at the moment) so a colour theme to match would be great.

It is crucial that the design communicates the beautiful nature of New Zealand, non-polluted environments, with emphasis on pure, natural and cleaniness.
Updates

A website that I quite like is http://www.frostvalegelato.co.nz

Information is easy to find, layout is nice and clear.                          

Hi all, I have now uploaded a logo for the business "Tidal Basket", please note that this is yet to be finalized however I expect it to be minor changes so please ensure the website theme and colour use go well with the logo. 

There are three scenery images uploaded, designs with any one of them used is fine whichever works better with your design.  Only one image is required on the website, no sliding effects for this.

Also just to clarify my requirements further.  The developer can use HTML, PHP, Javascript, CSS for coding, preferably to have the images cut and a pdf guide provided for things like alignment and sizing etc.

The menu items are Home / Our story / Product outline / Brands / Contact us
Designs are required for all these.  Within the product outline page, the subcategories are -
Infant formulas
Baby supplements
Toddlers products
Honey
Beauty products
Mens supplements
Womens supplements
Health products
Others

   

Target Market(s)

China based customers looking for quality products from New Zealand.

Industry/Entity Type

Health

Requirements
Must have
• clear menu bar in home page, the four main menu items are -
Our story
Product outline
Brands
Contact us
Nice to have
• Space for a large scenery photo in the home page

```html
<!DOCTYPE html>
<html lang="en">
<head>
<meta charset="utf-8">
<title>Tidal Basket – Our Story</title>
<link rel="stylesheet" href="https://fonts.googleapis.com/css2?family=Open+Sans:wght@400;600&family=Noto+Sans+SC:wght@400&display=swap">
<style>
:root{
  --brand-green:#78b643;
  --brand-dark:#313542;
  --footer-bg:#2f3240;
  --white:#ffffff;
  --nav-text:#333333;
  --footer-text:#d9dbe2;
}
*{margin:0;padding:0;box-sizing:border-box}
html,body{width:685px;height:1200px;overflow:hidden}
body{position:relative;font-family:"Open Sans",Arial,sans-serif;background:var(--brand-green);color:var(--white)}
.abs{position:absolute}

/* header */
.site-header{left:0;top:0;width:685px;height:34px;background:var(--white);box-shadow:0 1px 2px rgba(0,0,0,.2);z-index:2}
.brand-name{font-weight:600;color:var(--brand-green);white-space:nowrap}
.site-header .brand-name{left:136px;top:6px;font-size:17px}
.main-nav{top:8px;text-align:center;transform:translateX(-50%);color:var(--nav-text);line-height:8px}
.main-nav .zh{font-family:"Noto Sans SC","Open Sans",sans-serif;font-size:5.5px;color:#666}
.main-nav .en{font-size:6px;white-space:nowrap}
.nav-sep{top:8px;width:1px;height:16px;background:#e2e2e2}
.header-phone{left:490px;top:10px;font-size:8px;color:var(--nav-text);font-weight:600;display:flex;align-items:center;gap:3px}

/* banner */
.page-banner{left:0;top:34px;width:685px;height:133px;
  background:linear-gradient(180deg,#5f6b78 0%,#8a8577 28%,#9a7a45 48%,#6b5a32 62%,#3b3a2a 78%,#2a2a22 100%)}
.banner-band{left:0;top:134px;width:685px;height:33px;background:rgba(20,20,16,.55)}
.banner-title{left:137px;top:140px;font-size:15px;font-weight:400;color:var(--white)}

/* content */
h2{font-weight:400;font-size:12px;line-height:14px}
p.copy{font-size:5.4px;line-height:9.9px;letter-spacing:-.05px}
.logo-disc{left:136px;top:184px;width:132px;height:132px;border-radius:50%;background:var(--white);display:flex;align-items:center;justify-content:center}
.logo-disc .brand-name{font-size:18px}

.team-photo{width:69px;height:69px;border-radius:50%;background:radial-gradient(circle at 50% 40%,#8a8a8a,#3a3a3a 70%)}
.team-member{top:537px;width:100px;text-align:center;transform:translateX(-50%)}
.team-member .team-photo{margin:0 auto 8px}
.team-member .name{font-size:6.5px;line-height:7px}
.team-member .role{font-size:5.5px;line-height:7px}

.place-photo{width:131px;height:131px;border-radius:50%}

/* footer */
.site-footer{left:0;top:1104px;width:685px;height:96px;background:var(--footer-bg);color:var(--footer-text)}
.footer-title{font-size:6.5px;color:var(--white);letter-spacing:.2px}
.footer-list{list-style:none;font-size:5.6px;line-height:9.8px}
.footer-list.arrowed li::before{content:"›";margin-right:3px;color:var(--white)}
.contact-list{list-style:none;font-size:5.6px;line-height:9.8px}
.contact-list li{display:flex;align-items:flex-start;gap:3px}
.contact-list li.two-line{line-height:7.5px;margin-bottom:2px}
.contact-list svg{margin-top:2px;flex:none}
.site-footer .brand-name{font-size:16px}
.copyright{font-size:5.6px;color:var(--white)}
.social-dot{width:16px;height:16px;border-radius:50%}
</style>
</head>
<body>

<header class="site-header abs">
  <div class="brand-name abs">Tidal Basket</div>
  <nav>
    <div class="main-nav abs" style="left:274px"><div class="zh">主页</div><div class="en">HOME</div></div>
    <div class="nav-sep abs" style="left:295px"></div>
    <div class="main-nav abs" style="left:317px"><div class="zh">关于我们</div><div class="en">ABOUT US</div></div>
    <div class="nav-sep abs" style="left:340px"></div>
    <div class="main-nav abs" style="left:365px"><div class="zh">产品</div><div class="en">⌄ PRODUCTS</div></div>
    <div class="nav-sep abs" style="left:390px"></div>
    <div class="main-nav abs" style="left:410px"><div class="zh">品牌</div><div class="en">BRAND</div></div>
    <div class="nav-sep abs" style="left:430px"></div>
    <div class="main-nav abs" style="left:457px"><div class="zh">联系我们</div><div class="en">CONTACT US</div></div>
  </nav>
  <div class="header-phone abs">
    <svg width="7" height="8" viewBox="0 0 10 12"><path d="M2 0h2l1 3-1.5 1.2a7 7 0 0 0 3 4L8 7l2 1v2.5C10 11 9 12 8 12 3 11 0 6 0 2 0 1 1 0 2 0z" fill="#333"/></svg>
    027 555 0182
  </div>
</header>

<div class="page-banner abs" role="img" aria-label="Wide New Zealand landscape: sunlit golden mountain range under cloudy sky, autumn trees and open plain"></div>
<div class="banner-band abs"></div>
<h1 class="banner-title abs">Our Story</h1>

<main>
  <section class="story">
    <div class="logo-disc abs"><span class="brand-name">Tidal Basket</span></div>
    <h2 class="abs" style="left:285px;top:193px;font-size:14px">Our Story</h2>
    <p class="copy abs" style="left:285px;top:213px;width:260px">Sed quia consequuntur magni dantium, totam rem aperiam, eaque ipsa quae ab illo inventore veritatis et quasi archiecto beata. Vitae dicta sunt explicabo. Nemo enim ipsam voluptatem quia voluptas sit aspernatur aut odit aut fugit, sed quia consequuntur magni dantium, totam rem aperiam, eaque ipsa quae s et quasi architecto beata. Daut odit aut fugit, sed beata. Vitae dicta sunt explicabo.</p>
    <p class="copy abs" style="left:285px;top:272px;width:260px">Nemo enim ipsam voluptatem quia voluptas sit aspernatur aut odit aut fugit, sed quia consequuntur lorem ipsum metat id sim malaki ang butas ng ilong mo magni dantium, totam rem aperiam, eaque ipsa quae ab illo inventore veritatis et quasi architecto lorem ipsum dolor feeman beata.</p>
  </section>

  <section class="about">
    <h2 class="abs" style="left:138px;top:340px">Lorem Ipsum?</h2>
    <p class="copy abs" style="left:138px;top:360px;width:415px">Sed quia consequuntur magni dantium, totam rem aperiam, eaque ipsa quae ab illo inventore veritatis et quasi architecto beata. Vitae dicta sunt explicabo. Nemo enim ipsam voluptatem quia voluptas sit aspernatur aut odit aut fugit, sed quia consequuntur magni dantium, totam rem aperiam, eaque ipsa quae s et quasi architecto beata. Daut odit aut fugit, sed quia consequuntur magni dantium, totam rem aperiam, eaque ipsa quae ab illo inventore veritatis et quasi architecto beata. Vitae dicta sunt explicabo.</p>
    <p class="copy abs" style="left:138px;top:413px;width:415px">Nemo enim ipsam voluptatem quia voluptas sit aspernatur aut odit aut fugit, sed quia consequuntur lorem ipsum metat id sim malaki ang butas ng ilong mo magni dantium, totam rem aperiam, eaque ipsa quae ab illo inventore veritatis et quasi architecto lorem ipsum dolor feeman beata.</p>
  </section>

  <section class="team">
    <h2 class="abs" style="left:135px;top:465px">Meet the Team</h2>
    <p class="copy abs" style="left:135px;top:484px;width:415px">Sed quia consequuntur magni dantium, totam rem aperiam, eaque ipsa quae ab illo inventore veritatis et quasi architecto beata. Vitae dicta sunt explicabo. Nemo enim ipsam voluptatem quia voluptas sit aspernatur aut odit aut fugit, sed quia consequuntur magni dantium, totam rem aperiam, eaque ipsa quae s et quasi architecto beata.</p>
    <div class="team-member abs" style="left:184px"><div class="team-photo" role="img" aria-label="Portrait photo of team member"></div><div class="name">John Doe Smith</div><div class="role">Director</div></div>
    <div class="team-member abs" style="left:284px"><div class="team-photo" role="img" aria-label="Portrait photo of team member"></div><div class="name">Jane Anderson</div><div class="role">Marketing Executive</div></div>
    <div class="team-member abs" style="left:380px"><div class="team-photo" role="img" aria-label="Portrait photo of team member"></div><div class="name">John Doe Smith</div><div class="role">Director</div></div>
    <div class="team-member abs" style="left:481px"><div class="team-photo" role="img" aria-label="Portrait photo of team member"></div><div class="name">Jane Anderson</div><div class="role">Marketing Executive</div></div>
  </section>

  <section class="places">
    <h2 class="abs" style="left:138px;top:660px">Maybe Some Images for Office and Warehouses</h2>
    <p class="copy abs" style="left:138px;top:679px;width:415px">Sed quia consequuntur magni dantium, totam rem aperiam, eaque ipsa quae ab illo inventore veritatis et quasi architecto beata. Vitae dicta sunt explicabo. Nemo enim ipsam voluptatem quia voluptas sit aspernatur aut odit aut fugit, sed quia consequuntur magni dantium, totam rem aperiam, eaque ipsa quae s et quasi architecto beata. Daut odit aut fugit, sed quia consequuntur magni dantium, totam rem aperiam, eaque ipsa quae ab illo inventore veritatis et quasi architecto beata. Vitae dicta sunt explicabo.</p>
    <div class="place-photo abs" style="left:137px;top:738px;background:linear-gradient(135deg,#8a6a3e,#d0a36a 55%,#6b4f2c)" role="img" aria-label="Warehouse shelves stacked with cardboard boxes"></div>
    <div class="place-photo abs" style="left:277px;top:738px;background:linear-gradient(135deg,#8cc63f,#e9f0df 55%,#b9c9a0)" role="img" aria-label="Bright green office with desk and chair by a window"></div>
    <div class="place-photo abs" style="left:416px;top:738px;background:linear-gradient(180deg,#e6e6e3,#b9b8b3 60%,#6e6d6a)" role="img" aria-label="Open plan office with desks and chairs"></div>
    <div class="place-photo abs" style="left:137px;top:884px;background:linear-gradient(135deg,#d9e2dc,#f5f5f2 50%,#8c9190)" role="img" aria-label="Modern office workspace with staff at desks"></div>
    <div class="place-photo abs" style="left:277px;top:884px;background:linear-gradient(180deg,#b38a56,#d7b07a 50%,#5c6a80)" role="img" aria-label="Warehouse racking with boxed stock"></div>
    <div class="place-photo abs" style="left:416px;top:884px;background:linear-gradient(135deg,#8a6a46,#c79a66 45%,#5a7898)" role="img" aria-label="Warehouse worker carrying a carton"></div>
  </section>
</main>

<footer class="site-footer abs">
  <div class="footer-title abs" style="left:137px;top:16px">NAVIGATION</div>
  <ul class="footer-list abs" style="left:137px;top:28px">
    <li>Our Story</li><li>Support</li><li>Services</li><li>Legal</li><li>Sitemap</li>
  </ul>
  <div class="footer-title abs" style="left:199px;top:16px">PRODUCT OUTLINE</div>
  <ul class="footer-list arrowed abs" style="left:199px;top:28px">
    <li>Infant formulas</li><li>Baby supplements</li><li>Toddlers products</li><li>Honey</li><li>Beauty products</li>
  </ul>
  <ul class="footer-list arrowed abs" style="left:264px;top:28px">
    <li>Mens supplements</li><li>Women Supplements</li><li>Health Products</li><li>Others</li>
  </ul>
  <div class="footer-title abs" style="left:350px;top:16px">CONTACT US</div>
  <ul class="contact-list abs" style="left:348px;top:29px">
    <li class="two-line"><svg width="6" height="5" viewBox="0 0 12 10"><path d="M6 0l6 5h-2v5H7V7H5v3H2V5H0z" fill="#fff"/></svg><span>: PO Box 4815<br>&nbsp;&nbsp;Lorem City Country</span></li>
    <li><svg width="5" height="6" viewBox="0 0 10 12"><path d="M2 0h2l1 3-1.5 1.2a7 7 0 0 0 3 4L8 7l2 1v2.5C10 11 9 12 8 12 3 11 0 6 0 2 0 1 1 0 2 0z" fill="#fff"/></svg><span>: 1-800-555-019</span></li>
    <li><svg width="4" height="6" viewBox="0 0 8 12"><rect x="0.5" y="0.5" width="7" height="11" rx="1" fill="none" stroke="#fff"/><rect x="2" y="2" width="4" height="6" fill="#fff"/></svg><span>: 027 555 734</span></li>
    <li><svg width="6" height="5" viewBox="0 0 12 9"><rect x="0.5" y="0.5" width="11" height="8" fill="none" stroke="#fff"/><path d="M0.5 0.5L6 5l5.5-4.5" fill="none" stroke="#fff"/></svg><span>: info@tidalbasket.co.nz</span></li>
  </ul>
  <div class="brand-name abs" style="left:452px;top:20px">Tidal Basket</div>
  <div class="copyright abs" style="left:445px;top:43px">(c) Copyright 2013. All Rights Reserved</div>
  <div class="social-dot abs" style="left:479px;top:55px;background:#2fa4e0" aria-label="Social link"></div>
  <div class="social-dot abs" style="left:499px;top:55px;background:#3b5fa8" aria-label="Social link"></div>
</footer>

</body>
</html>
```